Simple templates for management consulting firm

Vireo Associates is a management consulting firm based in the DC area. We have all the basic templates but would like to tweak them so they look consistent.

Check us out at www.vireoassociates-example.com

For this project we would like to get
a tweaked powerpoint template (header should be up)
a letter template for letters
a fax template

Current templates and our logo are attached.
Updates

We just increased the budget of this project.

We got questions about the project. Here are our thoughts on this one:

Please include the logo into the fax template. If you find improvements in the layout then feel free to make those. Let's not overthink this too much. Keep it simple :)

We like The powerpoint concept as is. The slide titles are for some reasons on the bottom. It seems to irritate some folks. If you can switch the slide titles to the top, keep the look and feel of the slides and work in the logo then that would be fantastic.

The letter head should include the following

Vireo Associates, LLC Box 5827, Millbrook, VA 20147 Phone 703 518-9461, Fax 703 286 7135, www.vireoassociates-example.com and the logo.

Again, let's keep it simple.

Thank you for considering this project.

We just realize that we are not necessarily inisting to use the red in the slides.
Any approach that would work with the logo will be considered.

Thanks for your creativity.

Target Market(s)

tech companies, Pinnacle 400, venture capitalists

Industry/Entity Type

Management Consulting

Requirements
Must have
• Keep it simple please

```html
<!DOCTYPE html>
<html lang="en">
<head>
<meta charset="utf-8">
<title>Vireo Associates Stationery</title>
<link href="https://fonts.googleapis.com/css2?family=Open+Sans:wght@400;600&display=swap" rel="stylesheet">
<style>
  :root {
    --canvas: #ffffff;
    --paper: #f1eeeb;
    --brand-red: #b3242a;
    --brand-gold: #d4a13a;
    --brand-grey: #a9a7a4;
    --ink: #4a4a4a;
    --strip-dark: #3f3f3d;
    --window: #f6f5f3;
  }
  html, body {
    margin: 0;
    padding: 0;
    width: 1200px;
    height: 900px;
    overflow: hidden;
    background: var(--canvas);
    font-family: "Open Sans", Arial, sans-serif;
  }
  .stationery-set {
    position: relative;
    width: 1200px;
    height: 900px;
  }
  .letterhead {
    position: absolute;
    left: 50px;
    top: 62px;
    width: 580px;
    height: 746px;
    background: var(--paper);
    box-shadow: 1px 2px 4px rgba(0,0,0,0.25);
  }
  .letterhead-brand {
    position: absolute;
    left: 21px;
    top: 14px;
    display: flex;
    align-items: center;
    gap: 6px;
  }
  .brand-square {
    width: 14px;
    height: 14px;
    background: var(--brand-red);
  }
  .brand-name {
    font-weight: 600;
    font-size: 15px;
    letter-spacing: 0.5px;
    color: var(--brand-red);
  }
  .letterhead-footer {
    position: absolute;
    left: 13px;
    right: 13px;
    bottom: 10px;
    display: flex;
    align-items: flex-end;
    font-size: 7.5px;
    line-height: 10.5px;
    color: var(--ink);
  }
  .footer-address { width: 142px; }
  .footer-company { color: var(--brand-gold); }
  .footer-phones { flex: 1; }
  .footer-web { text-align: right; }
  .envelope {
    position: absolute;
    left: 491px;
    top: 337px;
    width: 656px;
    height: 291px;
    background: var(--paper);
    box-shadow: 1px 2px 5px rgba(0,0,0,0.3);
    overflow: hidden;
  }
  .envelope-strip {
    position: absolute;
    left: 0;
    top: 0;
    width: 19px;
    height: 100%;
    background: var(--strip-dark);
    border-right: 3px solid var(--brand-gold);
  }
  .envelope-brand {
    position: absolute;
    left: 34px;
    top: 20px;
    display: flex;
    align-items: center;
    gap: 7px;
  }
  .envelope-brand .brand-square { background: var(--brand-gold); width: 16px; height: 16px; }
  .envelope-brand .brand-name { color: var(--brand-gold); font-size: 17px; }
  .address-window {
    position: absolute;
    left: 51px;
    top: 186px;
    width: 234px;
    height: 64px;
    border-radius: 10px;
    background: var(--window);
    box-shadow: inset 0 1px 3px rgba(0,0,0,0.35);
  }
  .envelope-accent {
    position: absolute;
    right: 0;
    bottom: 0;
  }
</style>
</head>
<body>
<main class="stationery-set">
  <section class="letterhead" aria-label="Letterhead">
    <div class="letterhead-brand">
      <span class="brand-square"></span>
      <span class="brand-name">Vireo Associates</span>
    </div>
    <footer class="letterhead-footer">
      <div class="footer-address">
        <div class="footer-company">Vireo Associates</div>
        <div>LLC Box 5827, Millbrook, VA 20147</div>
      </div>
      <div class="footer-phones">
        <div>T: +1 703 518 9461</div>
        <div>F: +1 703 286 7135</div>
      </div>
      <div class="footer-web">www.vireoassociates-example.com</div>
    </footer>
  </section>

  <section class="envelope" aria-label="Window envelope">
    <div class="envelope-strip"></div>
    <div class="envelope-brand">
      <span class="brand-square"></span>
      <span class="brand-name">Vireo Associates</span>
    </div>
    <div class="address-window"></div>
    <svg class="envelope-accent" width="160" height="120" viewBox="0 0 160 120" aria-hidden="true">
      <circle cx="82" cy="112" r="78" fill="var(--brand-grey)"/>
    </svg>
  </section>
</main>
</body>
</html>
```